Buch-/E-Book-Cover für einen Eltern-Ratgeber
Zielgruppe
Ich bin Autor/Self-Publisher von Büchern/E-Books.
Aufgabenstellung
Ich benötige ein Buchcover (Print Paperback und E-Book) für einen kurzen Eltern-Ratgeber (ca. 60 Seiten):
Titel: 'Kleine Helden im Badezimmer'
Autorin: Frieda Wolkenstein
FW Verlag, Berlin
Das Buch richtet sich an verzweifelte Eltern und gibt Tipps, wie sie ihre kleinen Kinder zum Zähne putzen animieren können. Für die Gestaltung gerne vorzugsweise Fotos von echten Menschen (Eltern + Kind bzw. nur Kind bzw. 2 Kinder). Illustrierte Cover sind auch OK, aber nicht präferiert. Für Vorschläge bitte *inklusive Rückseite* und an bestehenden Eltern-Ratgebern orientieren, die Buchhafen zu finden sind, wie zum Beispiel:
- Wiegenzeit von Tilo K. Brenner
- PAPA im Takt von Nora Fendt
- Mutig durch den Alltag von Wiebke Tolan
- Grenzen setzen ohne Streit von Gudrun Vell-Borm
Auf den Buchseiten sind Illustrationen enthalten, die mit dem Buchcover möglichst auch harmonisieren sollten. Die Entwürfe der Illustrationen sind hier hochgeladen.
Ggf. kann man mit einer Text-Banderole/Kreis arbeiten, mit der Aufschrift '21 praktische Tipps für Eltern'
Klappentext:
Ihr Kind will sich partout nicht die Zähne putzen? Jedes Bitten und Flehen sind vergebens?
Für viele Eltern von kleinen Kindern ist es ein täglicher K(r)ampf im Bad. Ein ewiges Theater und langes Diskutieren. Niemand möchte sein Kind zwingen, schon gar nicht körperlich. Aber ohne Zähneputzen keine gesunden und schönen Zähne. Was also tun?
Nicht verzweifeln! Alle geplagten Eltern von Zwei- bis Fünfjährigen finden in diesem Büchlein 21 kurze und praktische Tipps, wie sie ihr Kind zum Zähneputzen animieren können. So wird das Zähneputzen ein fester Bestandteil der Morgen- und Abendroutine. Mit Spaß und Freude und ohne Graus. Probieren Sie die Tipps heute noch aus!

```html
<!DOCTYPE html>
<html lang="de">
<head>
<meta charset="utf-8">
<title>Kleine Helden im Badezimmer – Buchcover</title>
<link href="https://fonts.googleapis.com/css2?family=Bebas+Neue&family=Roboto+Condensed:wght@400&family=Barlow:wght@600&family=Allura&family=Merriweather:wght@900&display=swap" rel="stylesheet">
<style>
  :root {
    --purple: #8a5ca8;
    --purple-deep: #7a4f9c;
    --pink: #e6338f;
    --ink: #1f1f1f;
    --stage: #f1f1f1;
    --paper-top: #fbfbfb;
    --paper-bottom: #dcdcde;
    --white: #ffffff;
  }
  * { box-sizing: border-box; margin: 0; padding: 0; }
  html, body { width: 1200px; height: 1195px; overflow: hidden; background: var(--stage); }
  .canvas { position: relative; width: 1200px; height: 1195px; }

  .cover { position: absolute; top: 200px; width: 540px; height: 790px; overflow: hidden; box-shadow: 0 10px 30px rgba(0,0,0,.12); }
  .cover--front { left: 40px; }
  .cover--back { left: 620px; background: linear-gradient(180deg, var(--paper-top), var(--paper-bottom)); text-align: center; }

  .cover__photo { position: absolute; inset: 0;
    background:
      radial-gradient(ellipse 46% 36% at 52% 58%, #e9c4ad 0%, #d9b7a0 45%, rgba(217,183,160,0) 100%),
      radial-gradient(ellipse 60% 30% at 50% 95%, #f3f0ec 0%, rgba(243,240,236,0) 100%),
      linear-gradient(180deg, #fafafa 0%, #f1efed 45%, #e8e3df 100%); }

  .cover__author { position: absolute; top: 42px; width: 100%; text-align: center; font: 400 20px "Roboto Condensed", sans-serif; color: var(--ink); }
  .cover__title { position: absolute; top: 84px; width: 100%; text-align: center; font: 400 84px/0.86 "Bebas Neue", sans-serif; }
  .cover__title-line { display: block; }
  .cover__title-line--purple { color: var(--purple); }
  .cover__title-line--pink { color: var(--pink); }

  .badge { position: absolute; left: 82px; top: 612px; width: 140px; height: 140px; border-radius: 50%; background: var(--pink); color: var(--white); font-family: "Merriweather", serif; font-weight: 900; text-align: center; display: flex; flex-direction: column; justify-content: center; transform: rotate(-5deg); }
  .badge__number { font-size: 44px; line-height: 1; }
  .badge__word { font-size: 17px; font-weight: 900; line-height: 1.2; }
  .badge__tips { font-size: 26px; line-height: 1; }

  .banner { position: absolute; left: 216px; top: 652px; width: 292px; height: 76px; background: var(--purple-deep); transform: rotate(-3deg); display: flex; align-items: center; justify-content: center; }
  .banner__rule { position: absolute; left: 30px; top: -10px; width: 190px; height: 4px; background: var(--purple-deep); }
  .banner__text { font: 400 54px "Allura", cursive; color: var(--white); }

  .blurb__lead { margin: 92px 60px 0; font: 600 17px/1.4 "Barlow", sans-serif; letter-spacing: .06em; color: var(--purple); }
  .blurb__body { margin: 20px 54px 0; font: 400 14.5px/1.4 "Roboto Condensed", sans-serif; color: var(--ink); }
  .blurb__script { margin: 18px 0 12px; font: 400 50px/1.1 "Allura", cursive; color: var(--pink); }
  .blurb__cta { margin: 28px 0 0; font: 600 17px/1.4 "Barlow", sans-serif; letter-spacing: .06em; color: var(--purple); }
</style>
</head>
<body>
<main class="canvas">
  <section class="cover cover--front">
    <div class="cover__photo" role="img" aria-label="Foto: lachendes Kleinkind mit Zöpfchen putzt sich mit einer pink-lila Zahnbürste die Zähne, heller Hintergrund"></div>
    <p class="cover__author">Frieda Wolkenstein</p>
    <h1 class="cover__title">
      <span class="cover__title-line cover__title-line--purple">Kleine Helden</span>
      <span class="cover__title-line cover__title-line--pink">im Badezimmer</span>
    </h1>
    <div class="banner"><span class="banner__rule"></span><span class="banner__text">für Eltern</span></div>
    <div class="badge">
      <span class="badge__number">21</span>
      <span class="badge__word">praktische</span>
      <span class="badge__tips">TIPPS</span>
    </div>
  </section>

  <section class="cover cover--back">
    <p class="blurb__lead">Ihr Kind will sich partout nicht die Zähne putzen? Jedes Bitten und Flehen ist vergebens?</p>
    <p class="blurb__body">Für viele Eltern von kleinen Kindern ist es ein täglicher K(r)ampf im Bad. Ein ewiges Theater und langes Diskutieren. Niemand möchte sein Kind zwingen, schon gar nicht körperlich. Aber ohne Zähneputzen keine gesunden und schönen Zähne. Was also tun?</p>
    <p class="blurb__script">Nicht verzweifeln!</p>
    <p class="blurb__body">Alle geplagten Eltern von Zwei- bis Fünfjährigen finden in diesem Büchlein 21 kurze und praktische Tipps, wie sie Ihr Kind zum Zähneputzen animieren können. So wird das Zähneputzen ein fester Bestandteil der Morgen- und Abendroutine. Mit Spaß und Freude und ohne Graus.</p>
    <p class="blurb__cta">Probieren Sie die Tipps<br>heute noch aus!</p>
  </section>
</main>
</body>
</html>
```